Commercial wall and ceiling contractor needs website

Construction trade companies are notoriously behind the rest of the world when it comes to using current technology to run their businesses; we are not one of those companies. We are a walls and ceilings contractor using up to date communications technologies and applying them unlike any other in our trade. As simple as it sounds, and it really is that simple, it is still a new idea in the trade. We are moving our customers towards communicating with us through a single point of contact using text and email; we distribute information to the appropriate internal party on our end. We need a website that generally appears traditionally familiar to the visitor while also expresses a fresh new approach and edginess to the trade business.

Target Market(s)

General contractors looking to get a bit of background info before inviting us to bid on their projects. This is not a high traffic environment. Their subsequent site visits will be primarily for contact info.

Industry/Entity Type

Construction Company

Number of Pages Required

3 page

Font styles to use
Sans Serif

Requirements
Must have
• The file I uploaded named "plomsite.docx" does not have to appear on the site in the same manner in which appears in the document file; but the info contained within that document does need to be represented on the site.

```html
<!DOCTYPE html>
<html lang="en">
<head>
<meta charset="utf-8">
<title>Plomsite — Commercial Wall and Ceiling Contractor</title>
<link href="https://fonts.googleapis.com/css2?family=Raleway:wght@400;500;600;700&display=swap" rel="stylesheet">
<style>
:root{
  --gold:#b27b24;
  --gold-dark:#9a6a1c;
  --green:#1e5e3f;
  --green-dark:#174d33;
  --ink:#2b2b2b;
  --text:#3a3a3a;
  --muted:#8a8a8a;
  --line:#e2e2e2;
  --paper:#f5f5f5;
  --white:#fff;
}
*{margin:0;padding:0;box-sizing:border-box}
html,body{width:1200px;height:3801px;overflow:hidden;background:var(--white)}
body{font-family:"Raleway",sans-serif;color:var(--text);font-size:14px}
.wrap{position:relative;width:1020px;margin:0 auto;height:100%}
a{color:inherit;text-decoration:none}

/* top bar */
.topbar{height:49px;background:var(--gold);color:var(--white);font-size:16px}
.topbar .wrap{display:flex;align-items:center;justify-content:space-between}
.topbar-right{display:flex;align-items:center;gap:28px}
.social-dots{display:flex;gap:10px}
.social-dots span{width:12px;height:12px;border-radius:50%;background:var(--white);opacity:.9}
.lang{font-size:16px}
.lang::after{content:"";display:inline-block;margin-left:6px;border:5px solid transparent;border-top-color:var(--white);vertical-align:-2px}

/* header */
.header{height:143px;border-bottom:1px solid var(--line)}
.brand{position:absolute;left:0;top:20px;display:flex;align-items:center;gap:12px}
.brand-box{width:40px;height:40px;border:4px solid var(--gold)}
.brand-name{font-size:34px;font-weight:700;color:var(--gold);letter-spacing:3px}
.contact-strip{position:absolute;right:0;top:24px;display:flex;gap:24px;font-size:16px;color:var(--ink);line-height:28px}
.contact-item{display:flex;align-items:center;gap:10px}
.icon-circle{width:40px;height:40px;border-radius:50%;border:3px solid var(--green);display:flex;align-items:center;justify-content:center}
.contact-item b{font-weight:700}
.nav{position:absolute;right:0;top:104px;display:flex;gap:42px;font-size:17px;color:var(--ink)}

/* hero */
.hero{position:relative;height:580px;background:linear-gradient(100deg,#8f7e6a 0%,#b8ab98 40%,#d6cfc5 70%,#cfc8be 100%)}
.hero-photo{position:absolute;inset:0;background:linear-gradient(180deg,rgba(70,60,50,.25),rgba(120,110,100,.1))}
.hero-copy{position:absolute;left:90px;top:145px;color:var(--white)}
.hero-copy h1{font-size:55px;font-weight:500;letter-spacing:1px;line-height:1.2}
.hero-copy p{font-size:27px;font-weight:500;line-height:54px;margin-top:10px;width:640px}
.btn-pill{display:inline-flex;align-items:center;gap:10px;background:var(--gold);color:var(--white);font-weight:700;border-radius:30px;font-size:19px}
.hero .btn-pill{margin-top:22px;padding:16px 40px}
.arrow-dot{width:18px;height:18px;border-radius:50%;background:var(--white);position:relative}
.arrow-dot::after{content:"";position:absolute;left:6px;top:5px;border:4px solid transparent;border-left:6px solid var(--gold)}

.banner{height:90px;background:var(--green);color:var(--white);font-size:17px}
.banner .wrap{display:flex;align-items:center;justify-content:space-between}
.banner .btn-pill{padding:16px 42px}

/* section titles */
.sec-title{font-size:36px;font-weight:500;color:var(--green)}
.rule{height:1px;background:var(--line);position:relative;margin-top:16px}
.rule::before{content:"";position:absolute;left:0;top:-1px;width:55px;height:3px;background:var(--gold)}

/* about */
.about{height:695px}
.about-col{position:absolute;top:73px;width:492px}
.about-col.left{left:0}
.about-col.right{left:523px;width:497px}
.about-imgs{display:flex;gap:27px;margin-top:55px}
.about-imgs div{width:235px;height:173px}
.img-office{background:linear-gradient(180deg,#c9cfd4,#8e9aa3)}
.img-ceiling{background:linear-gradient(160deg,#e7e7e5,#b7bcc3)}
.tabs{display:flex;margin-top:19px;border:1px solid var(--line);height:66px}
.tabs span{flex:1;display:flex;align-items:center;justify-content:center;color:var(--gold);font-size:15px}
.tabs span+span{border-left:1px solid var(--line)}
.about-text{margin-top:12px;font-size:13.5px;line-height:31px;text-align:justify;color:var(--ink)}
.quote-box{margin-top:55px;border:1px solid var(--line);height:422px;padding:35px 36px}
.field-row{display:flex;gap:26px;margin-bottom:18px}
.field{width:200px;height:44px;border:1px solid var(--line);color:var(--muted);font-size:14px;padding:14px 12px}
.field.area{width:426px;height:132px}
.submit-row{display:flex;gap:18px;margin-top:20px}
.btn-submit{width:136px;height:48px;background:var(--gold);color:var(--white);font-size:18px;display:flex;align-items:center;justify-content:center;gap:6px}
.note{font-size:17px;line-height:30px;color:var(--ink)}
.note em{font-style:normal;color:var(--gold)}

/* projects */
.projects{height:647px;background:linear-gradient(135deg,#c2862c 0%,#b27b24 50%,#9c6a1f 100%)}
.projects .sec-title{color:var(--white);position:absolute;top:82px;left:3px}
.projects .rule{position:absolute;top:138px;left:3px;width:1017px;background:rgba(255,255,255,.3);margin:0}
.cards{position:absolute;top:180px;left:0;display:flex;gap:19px}
.card{width:328px;height:384px;background:var(--white);text-align:center}
.card-img{height:194px}
.p1{background:linear-gradient(180deg,#dfe6ec,#7f8f9c)}
.p2{background:linear-gradient(180deg,#eceeef,#a5aaae)}
.p3{background:linear-gradient(180deg,#8fa7bd,#d4dce3)}
.card h3{font-size:18px;font-weight:500;color:var(--gold);margin-top:22px}
.card p{font-size:12.5px;line-height:25px;padding:0 10px;margin-top:10px;text-align:justify;text-align-last:center;color:var(--ink)}
.card .more{display:block;color:var(--green);font-size:16px;font-weight:600;margin-top:6px}

/* reviews */
.reviews{height:522px}
.reviews .sec-title{position:absolute;top:80px;width:100%;text-align:center}
.reviews .center-rule{position:absolute;top:131px;left:4px;right:4px;height:2px;background:var(--line)}
.review-row{position:absolute;top:180px;display:flex;gap:27px}
.review{width:496px;height:202px;border:1px solid var(--line);padding:44px 18px 0 36px;display:flex;gap:18px}
.avatar{flex:none;width:72px;height:72px;background:linear-gradient(180deg,#c9c1b8,#8c8279)}
.review h4{font-size:22px;font-weight:500;color:var(--green)}
.review .role{font-size:13px;color:var(--gold);margin-top:2px}
.review p{font-size:12.5px;line-height:25px;text-align:justify;margin-top:4px;color:var(--ink)}
.dots{position:absolute;top:2425px;}
.pager{position:absolute;top:251px;left:0;width:100%;display:flex;justify-content:center;gap:18px}
.pager span{width:9px;height:9px;border-radius:50%;border:1px solid #ddd}
.pager span.on{background:var(--gold);border-color:var(--gold)}

/* news */
.news{height:647px;background:linear-gradient(135deg,#2a7550 0%,#1e5e3f 55%,#184f35 100%);color:var(--white)}
.news .sec-title{color:var(--white);position:absolute;top:85px;left:3px}
.news .rule{position:absolute;top:138px;left:3px;width:1017px;background:rgba(255,255,255,.3);margin:0}
.news-cards{position:absolute;top:182px;left:0;display:flex;gap:19px}
.news-card{width:328px}
.news-img{height:192px;position:relative}
.n1{background:linear-gradient(180deg,#e6e6e4,#8a8680)}
.n2{background:linear-gradient(180deg,#8a6a50,#d9b48a)}
.n3{background:linear-gradient(90deg,#b29372,#2a2a2a 45%,#eaeaea 70%)}
.date{position:absolute;right:12px;top:14px;background:var(--gold);color:var(--white);font-size:16px;padding:4px 10px}
.news-card h3{font-size:18px;font-weight:500;margin-top:20px;padding-left:3px}
.news-card p{font-size:12.5px;line-height:25px;margin-top:8px;text-align:justify;padding:0 14px 0 3px}
.news-card .more{display:block;font-size:16px;font-weight:600;margin-top:6px;padding-left:2px}

/* footer */
.footer{height:357px;background:var(--paper)}
.f-brand{position:absolute;left:0;top:140px}
.f-brand .brand-name{font-size:24px;letter-spacing:2px}
.f-brand .brand-box{width:30px;height:30px;border-width:3px}
.f-social{display:flex;gap:6px;margin:16px 0 0 34px}
.f-social span{width:26px;height:26px;border-radius:50%;border:1.5px solid var(--ink)}
.f-col{position:absolute;top:100px}
.f-col h5{font-size:20px;font-weight:700;color:var(--ink)}
.f-news{left:235px;width:295px}
.f-news p{font-size:12.5px;line-height:21px;margin-top:14px;color:var(--ink)}
.f-input{margin-top:12px;height:44px;border:1px solid #ddd;background:var(--white);font-size:12px;padding:14px 14px;color:var(--ink)}
.f-btn{margin-top:18px;display:inline-block;background:var(--gold);color:var(--white);font-size:13px;font-weight:600;padding:12px 20px}
.f-contact{left:571px;width:300px}
.f-contact ul,.f-links ul{list-style:none;margin-top:26px}
.f-contact li{display:flex;gap:18px;font-size:14px;line-height:22px;color:var(--ink);margin-bottom:12px}
.f-contact li i{flex:none;width:12px;height:12px;background:var(--green);margin-top:5px}
.f-links{left:884px}
.f-links li{font-size:14px;line-height:31.5px;color:var(--ink)}
.f-links ul{margin-top:14px}
.copyright{height:71px;border-top:1px solid var(--line);text-align:center;font-size:14px;line-height:70px;color:var(--ink)}
</style>
</head>
<body>

<div class="topbar">
  <div class="wrap">
    <span>We are a Commercial wall and ceiling contractor</span>
    <div class="topbar-right">
      <div class="social-dots"><span></span><span></span><span></span><span></span><span></span></div>
      <span class="lang">English</span>
    </div>
  </div>
</div>

<header class="header">
  <div class="wrap">
    <div class="brand"><span class="brand-box"></span><span class="brand-name">PLOMSITE</span></div>
    <div class="contact-strip">
      <div class="contact-item">
        <span class="icon-circle"><svg width="18" height="18" viewBox="0 0 24 24"><path d="M12 2a7 7 0 0 0-7 7c0 5 7 13 7 13s7-8 7-13a7 7 0 0 0-7-7zm0 9.5A2.5 2.5 0 1 1 12 6.5a2.5 2.5 0 0 1 0 5z" fill="#1e5e3f"/></svg></span>
        <span>2240 Harlow Creek Road,<br>Kelton, TX - 75510</span>
      </div>
      <div class="contact-item">
        <span class="icon-circle"><svg width="18" height="18" viewBox="0 0 24 24"><path d="M6.6 10.8a15 15 0 0 0 6.6 6.6l2.2-2.2a1 1 0 0 1 1-.25 11.4 11.4 0 0 0 3.6.57 1 1 0 0 1 1 1V20a1 1 0 0 1-1 1A17 17 0 0 1 3 4a1 1 0 0 1 1-1h3.5a1 1 0 0 1 1 1c0 1.25.2 2.45.57 3.57a1 1 0 0 1-.25 1z" fill="#1e5e3f"/></svg></span>
        <span><b>555-014-2290</b><br>office@plomsitewalls.com</span>
      </div>
    </div>
    <nav class="nav"><a>Home</a><a>About</a><a>Our Services</a><a>Latest News</a><a>Testimonials</a><a>Contact Us</a></nav>
  </div>
</header>

<section class="hero">
  <div class="hero-photo" role="img" aria-label="Stone-clad commercial building entrance with paved walkway and a wall-mounted sign"></div>
  <div class="hero-copy">
    <h1>WELCOME TO PLOMSITE</h1>
    <p>Sed ut perspiciatis unde omnis iste natus error sit voluptatem accusantium doloremque</p>
    <a class="btn-pill">Contact Us <span class="arrow-dot"></span></a>
  </div>
</section>

<div class="banner">
  <div class="wrap">
    <span>We can't control the weather, but we can control the schedule, costs, quality and safety.</span>
    <a class="btn-pill">Contact Us <span class="arrow-dot"></span></a>
  </div>
</div>

<section class="about">
  <div class="wrap">
    <div class="about-col left">
      <h2 class="sec-title">About us</h2>
      <div class="rule"></div>
      <div class="about-imgs">
        <div class="img-office" role="img" aria-label="Modern office interior with glass partition walls"></div>
        <div class="img-ceiling" role="img" aria-label="Worker installing a fixture in a ceiling"></div>
      </div>
      <div class="tabs"><span>Commercial wall</span><span>ceiling contractor</span></div>
      <p class="about-text">Sed ut perspiciatis unde omnis iste natus error sit voluptatem accusantium doloremque laudantium, totam rem aperiam, eaque ipsa quae ab illo inventore veritatis et quasi architecto beatae vitae dicta sunt explicabo. Nemo enim ipsam voluptatem quia voluptas sit aspernatur aut odit aut fugit, sed quia consequuntur magni dolores eos qui ratione voluptatem sequi nesciunt.</p>
    </div>
    <div class="about-col right">
      <h2 class="sec-title">Request a Free Quote</h2>
      <div class="rule"></div>
      <div class="quote-box">
        <div class="field-row"><div class="field">Your Name</div><div class="field">Email id</div></div>
        <div class="field-row"><div class="field">Phone Number</div><div class="field">Subject</div></div>
        <div class="field area"></div>
        <div class="submit-row">
          <div class="btn-submit"><svg width="16" height="16" viewBox="0 0 24 24"><path d="M2 11 22 2l-6 20-4-8-10-3zm10 3 9-11" fill="none" stroke="#fff" stroke-width="2"/></svg>SUBMIT</div>
          <p class="note"><em>Note:</em> We dont't do spam and<br>Your mail id very confidential.</p>
        </div>
      </div>
    </div>
  </div>
</section>

<section class="projects">
  <div class="wrap">
    <h2 class="sec-title">Our Projects</h2>
    <div class="rule"></div>
    <div class="cards">
      <div class="card"><div class="card-img p1" role="img" aria-label="Glass-facade office tower beside a city skyline"></div><h3>Sed ut perspiciatis unde omnis</h3><p>Sed ut perspiciatis unde omnis iste natus error sit voluptatem accusantium doloremque totam rem aperiam dicta sunt explicabo.</p><a class="more">Read more</a></div>
      <div class="card"><div class="card-img p2" role="img" aria-label="Large open interior with finished white ceiling and skylights"></div><h3>Sed ut perspiciatis unde omnis</h3><p>Sed ut perspiciatis unde omnis iste natus error sit voluptatem accusantium doloremque totam rem aperiam dicta sunt explicabo.</p><a class="more">Read more</a></div>
      <div class="card"><div class="card-img p3" role="img" aria-label="Empty office floor with floor-to-ceiling windows overlooking a city"></div><h3>Sed ut perspiciatis unde omnis</h3><p>Sed ut perspiciatis unde omnis iste natus error sit voluptatem accusantium doloremque totam rem aperiam dicta sunt explicabo.</p><a class="more">Read more</a></div>
    </div>
  </div>
</section>

<section class="reviews">
  <div class="wrap">
    <h2 class="sec-title">Client Reviews</h2>
    <div class="center-rule"></div>
    <div class="review-row">
      <div class="review"><div class="avatar" role="img" aria-label="Client portrait"></div><div><h4>Daniel Hargrove</h4><div class="role">Ceo - Westbrook Clinics</div><p>Sed ut perspiciatis unde omnis iste natus error sit volupt accusantium doloremque laudantium, totam rem aperia, eaque ipsa quae ab illo sunt explicabo.</p></div></div>
      <div class="review"><div class="avatar" role="img" aria-label="Client portrait"></div><div><h4>Daniel Hargrove</h4><div class="role">Ceo - Westbrook Clinics</div><p>Sed ut perspiciatis unde omnis iste natus error sit volupt accusantium doloremque laudantium, totam rem aperia, eaque ipsa quae ab illo sunt explicabo.</p></div></div>
    </div>
    <div class="pager"><span class="on"></span><span></span><span></span></div>
  </div>
</section>

<section class="news">
  <div class="wrap">
    <h2 class="sec-title">Latest News</h2>
    <div class="rule"></div>
    <div class="news-cards">
      <div class="news-card"><div class="news-img n1" role="img" aria-label="Workers on a lift painting a wall"><span class="date">May 05 2019</span></div><h3>Sed ut perspiciatis unde omnis</h3><p>Sed ut perspiciatis unde omnis iste natus error sit voluptatem accusantium doloremque totam rem aperiam dicta sunt explicabo.</p><a class="more">Read more</a></div>
      <div class="news-card"><div class="news-img n2" role="img" aria-label="Reception area with wood floor and paneled wall"><span class="date">May 05 2019</span></div><h3>Sed ut perspiciatis unde omnis</h3><p>Sed ut perspiciatis unde omnis iste natus error sit voluptatem accusantium doloremque totam rem aperiam dicta sunt explicabo.</p><a class="more">Read more</a></div>
      <div class="news-card"><div class="news-img n3" role="img" aria-label="Interior with stone-textured feature wall and plant"><span class="date">May 05 2019</span></div><h3>Sed ut perspiciatis unde omnis</h3><p>Sed ut perspiciatis unde omnis iste natus error sit voluptatem accusantium doloremque totam rem aperiam dicta sunt explicabo.</p><a class="more">Read more</a></div>
    </div>
  </div>
</section>

<footer class="footer">
  <div class="wrap">
    <div class="f-brand">
      <div class="brand" style="position:static"><span class="brand-box"></span><span class="brand-name">PLOMSITE</span></div>
      <div class="f-social"><span></span><span></span><span></span><span></span></div>
    </div>
    <div class="f-col f-news">
      <h5>SIGN UP FOR NEWSLETTER</h5>
      <p>Excepteur sint occaecat cupidatat non proident, sunt in culpa qui officia deserunt</p>
      <div class="f-input">Enter email</div>
      <span class="f-btn">SUBSCRIPTION</span>
    </div>
    <div class="f-col f-contact">
      <h5>CONTACT US</h5>
      <ul>
        <li><i></i><span>Phone: 555-014-2290</span></li>
        <li><i></i><span>Email:<br>office@plomsitewalls.com</span></li>
      </ul>
    </div>
    <div class="f-col f-links">
      <h5>QUICK LINKS</h5>
      <ul><li>Home</li><li>About us</li><li>Service</li><li>Latest News</li><li>Testimonials</li><li>Contact US</li></ul>
    </div>
  </div>
</footer>
<div class="copyright">Copyright © 2019. All rights reserved.</div>

</body>
</html>
```